Subway/Bus ad sign for a paid research study

We are looking for someone who can help design an effective advertisement sign for a paid research study. The ad will be displayed in subway stations/bus. The study involves fMRI and is conducted by a laboratory in the University of Kestrelmoor.

We prefer ppt images so we could edit. Dimensions should be 46”h x 60”w, but may vary in the final version depending on our needs.

The way we would like to choose the final design is by running a pretest on friendvale to pick the most attractive ad. Your submission would mean that you consent with this process.

Thank you for your consideration.

Target Market(s)

age 18-64, philadelphia

Requirements
Must have
• The ad must include the following information (we encourage you to come up with better/more catchy slogans)
• - We are looking for participants for a research study
• - This fMRI study is conducted by researchers at University of Kestrelmoor
• - Email KmoorLB7@psy.kestrelmoor-edu.org to see if you are eligible
• - University of Kestrelmoor Logo
• The ad may include the following information
• - Participants get paid up to $190
Nice to have
• original attractive illustrations are highly encouraged.
Should not have
• It seems like brain photos tend to scare people away. Maybe you could focus on using survey-related images or illustrated images of the brain (vs. fMRI scans).

```html
<!DOCTYPE html>
<html lang="en">
<head>
<meta charset="utf-8">
<title>We Need Your Brain – fMRI Research Study</title>
<link rel="stylesheet" href="https://fonts.googleapis.com/css2?family=Archivo+Black&family=Arimo:ital,wght@0,400;0,700;1,400;1,700&display=swap">
<style>
  :root {
    --navy: #1b2157;
    --white: #ffffff;
    --glow: #ffffff;
    --edge: #b9b9bd;
    --art-warm: rgba(236, 120, 40, 0.55);
    --art-mid: rgba(120, 170, 60, 0.45);
    --art-cool: rgba(40, 90, 170, 0.30);
  }
  * { margin: 0; padding: 0; box-sizing: border-box; }
  html, body { width: 783px; height: 1200px; overflow: hidden; background: var(--white); }
  body { font-family: "Arimo", Arial, sans-serif; color: var(--navy); }

  .poster { position: relative; width: 783px; height: 1200px; }

  .headline-band {
    position: absolute; top: 0; left: 0; width: 783px; height: 125px;
    background: var(--navy); display: flex; align-items: center; justify-content: center;
  }
  .headline {
    color: var(--white); font-family: "Archivo Black", "Arial Black", sans-serif;
    font-weight: 400; font-size: 50px; letter-spacing: 1px; white-space: nowrap;
  }

  .stage {
    position: absolute; top: 125px; left: 0; width: 783px; height: 875px;
    background: radial-gradient(ellipse 62% 58% at 50% 52%, var(--glow) 55%, var(--edge) 100%);
  }
  .subhead {
    position: absolute; top: 46px; width: 100%; text-align: center;
    font-weight: 700; font-size: 41px; letter-spacing: 1.3px; white-space: nowrap;
  }
  .art-area {
    position: absolute; left: 150px; top: 128px; width: 480px; height: 510px;
    background: radial-gradient(ellipse 50% 50% at 50% 48%, var(--art-warm) 0%, var(--art-mid) 40%, var(--art-cool) 70%, rgba(255,255,255,0) 100%);
  }
  .pay {
    position: absolute; top: 663px; width: 100%; text-align: center;
    font-weight: 700; font-size: 36px; letter-spacing: 0.8px; white-space: nowrap;
  }
  .contact {
    position: absolute; top: 744px; width: 100%; text-align: center;
    font-style: italic; font-size: 28px; line-height: 44px; white-space: nowrap;
  }
  .contact strong { font-weight: 700; }

  .credit {
    position: absolute; top: 1000px; left: 0; width: 391px; height: 200px;
    background: var(--navy); color: var(--white);
    display: flex; align-items: center; justify-content: center; text-align: center;
    font-size: 20px; line-height: 27px;
  }
  .institution {
    position: absolute; top: 1000px; left: 391px; width: 392px; height: 200px;
    display: flex; align-items: center; justify-content: center; gap: 14px;
  }
  .institution-mark { width: 60px; height: 60px; background: var(--navy); }
  .institution-name { font-weight: 700; font-size: 44px; color: var(--navy); }
</style>
</head>
<body>
<main class="poster">
  <header class="headline-band">
    <h1 class="headline">We Need Your Brain...</h1>
  </header>

  <section class="stage">
    <h2 class="subhead">...for an fMRI research study.</h2>
    <div class="art-area" role="img" aria-label="Illustration area: colourful overlapping speech bubbles grouped into a brain shape"></div>
    <p class="pay">Participants get paid up to $190</p>
    <p class="contact">Email <strong>KmoorLB7@psy.kestrelmoor-edu.org</strong><br>to see if you are eligible</p>
  </section>

  <footer>
    <p class="credit">This fMRI study is conducted<br>by researchers at<br>University of Kestrelmoor</p>
    <div class="institution">
      <span class="institution-mark"></span>
      <span class="institution-name">Kestrelmoor</span>
    </div>
  </footer>
</main>
</body>
</html>
```